Our Joint Journey - Orthopedic needs from one site

We need slides that help to educate users, interest investors and allow the complexity of the entire continuum of care to be explained so anyone can understand. Our Joint Journey is a Varnolo Health Company. Ourjointjourneyhub.com. We allow people to evaluate, educate and engage with providers from one site. Simplyfying orthopedic care and wellness from one site. Patients, doctors, personal trainers, therapist, nutritionist, yoga, gyms, athletic trainers and more can connect from one site

Target Market(s)

Investors, Patients, Doctors and wellness providers

Industry/Entity Type

Healthcare

Requirements
Must have
• Investor slides, sales slides, education, process....

```html
<!DOCTYPE html>
<html lang="en">
<head>
<meta charset="UTF-8">
<title>What Is Orthopedic – Our Joint Journey</title>
<link rel="stylesheet" href="https://fonts.googleapis.com/css2?family=Montserrat:wght@500;700;800&family=Open+Sans:wght@400;600&display=swap">
<style>
  :root {
    --paper: #ffffff;
    --ink: #111111;
    --brand-ink: #24263a;
    --leaf: #84c24f;
    --night: #0b1a6e;
    --deep: #07115a;
    --glow: #2fd3f0;
  }
  * { margin: 0; padding: 0; box-sizing: border-box; }
  html, body { width: 1200px; height: 900px; overflow: hidden; background: var(--paper); }
  .slide {
    position: relative;
    width: 1200px;
    height: 900px;
    background: var(--paper);
    color: var(--ink);
    overflow: hidden;
  }
  .running-head {
    position: absolute;
    top: 71px;
    font-family: "Montserrat", sans-serif;
    font-weight: 500;
    font-size: 15px;
    letter-spacing: 2.4px;
    text-transform: uppercase;
  }
  .running-head--site { left: 68px; }
  .running-head--page { right: 66px; }
  .slide-title {
    position: absolute;
    left: 68px;
    top: 250px;
    font-family: "Montserrat", sans-serif;
    font-weight: 800;
    font-size: 55px;
    line-height: 77px;
    letter-spacing: 6px;
    text-transform: uppercase;
  }
  .slide-body {
    position: absolute;
    left: 49px;
    top: 474px;
    width: 530px;
    font-family: "Open Sans", sans-serif;
    font-size: 17.4px;
    line-height: 25.6px;
  }
  .accent-block {
    position: absolute;
    left: 627px;
    top: 568px;
    width: 573px;
    height: 332px;
    background: var(--leaf);
  }
  .hero-visual {
    position: absolute;
    left: 717px;
    top: 247px;
    width: 366px;
    height: 404px;
    background:
      radial-gradient(ellipse 45% 50% at 50% 38%, rgba(47, 211, 240, 0.9) 0%, rgba(30, 120, 220, 0.55) 45%, rgba(11, 26, 110, 0) 80%),
      linear-gradient(180deg, var(--night) 0%, var(--deep) 100%);
  }
  .brand-tile {
    position: absolute;
    left: 1010px;
    top: 709px;
    width: 190px;
    height: 191px;
    background: var(--paper);
    display: flex;
    flex-direction: column;
    align-items: center;
    justify-content: center;
    gap: 10px;
  }
  .brand-tile__mark {
    width: 26px;
    height: 26px;
    border-radius: 50%;
    background: var(--brand-ink);
  }
  .brand-tile__name {
    font-family: "Montserrat", sans-serif;
    font-weight: 700;
    font-size: 24px;
    line-height: 26px;
    color: var(--brand-ink);
    text-align: center;
  }
</style>
</head>
<body>
  <main class="slide">
    <header>
      <p class="running-head running-head--site">Ourjointjourney</p>
      <p class="running-head running-head--page">Page 02</p>
    </header>

    <h1 class="slide-title">What is<br>orthopedic</h1>

    <p class="slide-body">Orthopedic surgery or orthopedics, is the branch of surgery concerned with conditions involving the musculoskeletal system. Orthopedic surgeons use both surgical and nonsurgical means to treat musculoskeletal trauma, spine diseases, sports injuries, degenerative diseases, infections, tumors, and congenital disorders.</p>

    <div class="accent-block"></div>

    <div class="hero-visual" role="img" aria-label="Illustration of a running figure in blue with the knee joint highlighted in orange"></div>

    <div class="brand-tile">
      <span class="brand-tile__mark"></span>
      <p class="brand-tile__name">Varnolo<br>Health</p>
    </div>
  </main>
</body>
</html>
```